New Web Site Design - Amber Ridge Telecom Solutions

We are looking for a completely new web site design. Amber Ridge Telecom Solutions is a full service company providing PBX and IP/Cloud Based phone systems. We also sell and install video camera surveillance systems and provide low voltage cabling services (CAT5 and CAT3). We are looking for something professional looking. We want to be able to showcase our vendor partners as well as be able to show photos of some of the work we have done. We will also want to be able to post PDF brochures as well as make changes to the website ourselves.

Target Market(s)

Commercial

Industry/Entity Type

Communication

Coding

Coded - Design and coding required

Number of Pages Required

5+ page

Font styles to use
Sans Serif

Colors
0455a3

Requirements
Must have
• Ability to upload PDF brochures
• Professional look and feel
• Ability to upload and easily insert job photos
• Thinking it should have at least 6 pages: Main page, phone systems and services page, carrier services page, video surveillance systems and service page, low voltage cabling services page, contact us page

```html
<!DOCTYPE html>
<html lang="en">
<head>
<meta charset="utf-8">
<title>Amber Ridge Telecom Solutions</title>
<link href="https://fonts.googleapis.com/css2?family=Open+Sans:wght@400;600;700;800&family=Raleway:wght@400;600;700&display=swap" rel="stylesheet">
<style>
:root{
  --brand:#0455a3;
  --brand-dark:#033a72;
  --brand-light:#1a78d0;
  --ink:#2b2f36;
  --muted:#6c737d;
  --paper:#ffffff;
  --mist:#f1f3f6;
  --night:#15181d;
  --line:#d9dee5;
}
*{box-sizing:border-box;margin:0;padding:0}
html,body{width:1200px;height:2952px;overflow:hidden}
body{font-family:"Open Sans",Arial,sans-serif;color:var(--ink);background:var(--paper);position:relative}
.container{position:relative;width:760px;margin:0 auto;height:100%}
section,header,footer,nav{position:relative;width:1200px}

/* hero */
.hero{height:352px;background:radial-gradient(circle at 62% 55%,#5aa3e6 0%,#1f5d97 22%,#1a2330 55%,#0c0f14 100%)}
.hero-box{position:absolute;left:248px;top:22px;width:232px;height:196px;background:rgba(4,85,163,.88);padding:24px 22px;color:#fff}
.hero-box h1{font-size:25px;line-height:29px;font-weight:800;letter-spacing:.5px}
.hero-box p{font-size:10px;line-height:14px;margin-top:16px;font-weight:600;letter-spacing:.8px}
.hero-dots{position:absolute;left:50%;bottom:22px;transform:translateX(-50%);display:flex;gap:10px}
.hero-dots span{width:9px;height:9px;border-radius:50%;background:rgba(255,255,255,.5)}
.hero-dots span:first-child{background:#fff}

/* nav */
.site-nav{height:36px;background:var(--paper);border-bottom:1px solid var(--line)}
.brand{position:absolute;left:0;top:9px;display:flex;align-items:center;gap:6px;font-size:11px;font-weight:700;color:var(--brand)}
.brand i{width:16px;height:16px;border-radius:50%;background:var(--brand);display:block}
.menu{position:absolute;left:232px;top:11px;display:flex;gap:26px;font-size:11px;color:var(--ink)}
.social{position:absolute;right:0;top:11px;display:flex;gap:10px}
.social span{width:13px;height:13px;border-radius:50%;background:var(--brand)}

/* welcome */
.welcome{height:172px;text-align:center;background:linear-gradient(#fff,#f4f6f9)}
.eyebrow{font-size:13px;letter-spacing:3px;color:var(--brand);font-weight:600;padding-top:30px}
.welcome h2{font-size:34px;font-weight:600;color:var(--ink);margin-top:4px}
.welcome p{font-size:12px;color:var(--muted);margin-top:10px;line-height:17px}

/* services band */
.services{height:232px;background:linear-gradient(180deg,var(--brand-light),var(--brand) 60%,var(--brand-dark));color:#fff}
.service-row{position:absolute;left:150px;right:150px;top:24px;display:flex;justify-content:space-between}
.service{width:130px;text-align:center}
.service svg{width:58px;height:58px}
.service h3{font-size:12px;font-weight:700;margin-top:6px}
.service p{font-size:9px;line-height:13px;margin-top:8px;opacity:.9}
.band-dots{position:absolute;left:50%;bottom:18px;transform:translateX(-50%);display:flex;gap:8px}
.band-dots span{width:7px;height:7px;border-radius:50%;background:rgba(255,255,255,.6)}

/* features */
.features{height:368px;background:linear-gradient(#fff,#eef1f5);text-align:center}
.features .eyebrow{color:var(--ink);padding-top:24px}
.features h2{font-family:"Raleway",sans-serif;font-size:40px;font-weight:700;color:var(--ink)}
.feature-grid{position:absolute;left:320px;top:116px;width:600px;display:grid;grid-template-columns:repeat(3,1fr);row-gap:40px;column-gap:20px;text-align:left}
.feature{display:flex;gap:8px}
.feature svg{width:26px;height:20px;flex:none}
.feature h4{font-size:11px;color:var(--brand);font-weight:700}
.feature p{font-size:9px;line-height:13px;color:var(--muted);margin-top:4px}

/* clients */
.clients{height:380px;background:linear-gradient(100deg,#1c2027,#2c313a 50%,#15181d);color:#fff}
.ring{position:absolute;left:170px;top:-56px;width:440px;height:440px;border-radius:50%;border:26px solid var(--brand)}
.ring-text{position:absolute;left:240px;top:24px;width:300px;text-align:center}
.ring-text h3{font-size:16px;font-weight:600;letter-spacing:1px}
.ring-text h5{font-size:10px;font-weight:700;letter-spacing:1px;margin-top:2px}
.ring-text p{font-size:10px;line-height:15px;margin-top:18px;opacity:.85}
.ring-text .author{font-weight:700;margin-top:14px;opacity:1}
.ring-dots{display:flex;gap:8px;justify-content:center;margin-top:18px}
.ring-dots span{width:6px;height:6px;border-radius:50%;background:#fff}
.client-side{position:absolute;left:780px;top:24px;width:170px;text-align:right}
.client-side h3{font-size:19px;line-height:24px;font-weight:400}
.client-side ul{list-style:none;margin-top:18px}
.client-side li{margin-bottom:12px}
.client-side li b{display:block;font-size:10px}
.client-side li span{font-size:9px;opacity:.8}

/* gallery */
.gallery{height:220px;background:linear-gradient(90deg,var(--brand-dark),var(--brand));color:#fff}
.gallery-text{position:absolute;left:268px;top:18px;width:160px}
.gallery-text h3{font-size:13px;font-weight:700;letter-spacing:1px}
.gallery-text p{font-size:9px;line-height:13px;margin-top:10px}
.btn-outline{display:inline-block;margin-top:14px;border:1px solid #fff;font-size:8px;padding:4px 10px;letter-spacing:1px}
.tiles{position:absolute;left:448px;top:16px;display:grid;grid-template-columns:repeat(3,148px);gap:8px}
.tile{height:88px}
.t1{background:linear-gradient(135deg,#0a1a44,#3a8ae8,#0b1640)}
.t2{background:linear-gradient(135deg,#0a2c5e,#6ec6ff,#0b2a52)}
.t3{background:linear-gradient(135deg,#1a0840,#c25fe0,#2a0a55)}
.t4{background:linear-gradient(135deg,#02122e,#1c6fd6,#030d22)}
.t5{background:linear-gradient(135deg,#0b2d4e,#7ab8f0,#123a66)}
.t6{background:linear-gradient(135deg,#2a0c4e,#e06ad0,#3d0d60)}

/* partners */
.partners{height:400px;text-align:center;background:var(--paper)}
.partners h2{font-size:38px;font-weight:700;color:var(--ink);padding-top:30px}
.partners .sub{font-size:12px;color:var(--brand);font-weight:600;letter-spacing:1px;margin-top:2px}
.partner-band{position:absolute;left:0;top:120px;width:1200px;height:240px;background:linear-gradient(#fff,#e6e9ee 50%,#fff)}
.partner-row{position:absolute;left:260px;right:260px;top:100px;display:flex;justify-content:space-between;align-items:center}
.partner{font-size:18px;font-weight:700;color:#555b63}
.arrow{position:absolute;top:104px;font-size:20px;color:var(--brand);font-weight:700}

/* contact */
.contact{height:700px}
.contact-head{height:140px;text-align:center}
.contact-head p{font-size:12px;color:var(--brand);font-weight:600;letter-spacing:1px;padding-top:24px}
.contact-head h2{font-size:36px;font-weight:600;color:var(--ink)}
.contact-photo{position:absolute;left:0;top:140px;width:1200px;height:560px;background:linear-gradient(90deg,#e8e4e0,#f7f5f3 40%,#eceae8 70%,#dcd8d4)}
.form-panel{position:absolute;left:280px;top:200px;width:380px;height:460px;background:#fff;padding:28px 26px;box-shadow:0 4px 18px rgba(0,0,0,.12)}
.field{margin-bottom:14px}
.field label{display:flex;justify-content:space-between;font-size:9px;color:var(--ink)}
.field label em{font-style:normal;color:var(--brand)}
.field div{height:26px;background:var(--mist);border:1px solid var(--line);margin-top:4px}
.field.msg div{height:130px}
.btn{display:inline-block;background:var(--brand);color:#fff;font-size:9px;font-weight:700;padding:6px 12px}
.info-panel{position:absolute;left:672px;top:200px;width:248px;height:360px;background:#fff;padding:16px;box-shadow:0 4px 18px rgba(0,0,0,.12)}
.info-panel h3{font-size:16px;font-weight:600}
.info-panel .lead{font-size:9px;color:var(--muted);line-height:13px}
.info-panel .cta{font-size:10px;color:var(--brand);font-weight:700;margin-top:4px}
.info-item{display:flex;gap:8px;margin-top:12px;font-size:9px;line-height:13px;color:var(--muted)}
.info-item svg{width:14px;height:14px;flex:none}
.map{margin-top:14px;height:86px;background:linear-gradient(135deg,#e9efe6,#dfe6ea)}

/* footer */
.site-footer{height:92px;background:var(--brand);color:#fff}
.site-footer p{position:absolute;left:260px;top:30px;font-size:9px;line-height:13px}
.to-top{position:absolute;left:588px;top:30px;width:24px;height:24px;border-radius:50%;background:#fff}
</style>
</head>
<body>

<header class="hero" role="img" aria-label="Hand holding a tablet surrounded by glowing communication icons">
  <div class="hero-box">
    <h1>PBX AND IP/CLOUD BASED PHONE SYSTEMS.</h1>
    <p>SIMPLY INNOVATIVE<br>SOLUTIONS FOR BUSINESS</p>
  </div>
  <div class="hero-dots"><span></span><span></span><span></span></div>
</header>

<nav class="site-nav">
  <div class="container">
    <div class="brand"><i></i>Amber Ridge Telecom Solutions</div>
    <div class="menu"><span>Home</span><span>Phone Systems</span><span>Services</span><span>Contact Us</span></div>
    <div class="social" aria-label="Social links"><span></span><span></span><span></span></div>
  </div>
</nav>

<section class="welcome">
  <p class="eyebrow">WELCOME TO</p>
  <h2>Amber Ridge Telecom Solutions</h2>
  <p>Lorem Ipsum is simply dummy text of the printing.<br>LOREM IPSUM IS SIMPLY DUMMY TEXT OF THE PRINTING.</p>
</section>

<section class="services">
  <div class="service-row">
    <div class="service">
      <svg viewBox="0 0 58 58"><circle cx="29" cy="29" r="27" fill="none" stroke="#fff" stroke-width="2"/><path d="M20 18c2-2 4-1 5 1l2 4c1 2 0 3-1 4 1 3 4 6 7 7 1-1 2-2 4-1l4 2c2 1 3 3 1 5-3 3-7 3-12-1-5-4-9-9-11-14-1-3 0-5 1-7z" fill="#fff"/></svg>
      <h3>Carrier Services</h3>
      <p>Reliable voice lines and data plans set up and managed for your office with local support.</p>
    </div>
    <div class="service">
      <svg viewBox="0 0 58 58"><circle cx="29" cy="29" r="27" fill="none" stroke="#fff" stroke-width="2"/><rect x="15" y="22" width="22" height="13" rx="2" fill="#fff"/><path d="M37 25l8-4v14l-8-4z" fill="#fff"/></svg>
      <h3>Video Surveillance Systems</h3>
      <p>Camera systems sold, installed and serviced to keep your site safe day and night.</p>
    </div>
    <div class="service">
      <svg viewBox="0 0 58 58"><circle cx="29" cy="29" r="27" fill="none" stroke="#fff" stroke-width="2"/><rect x="22" y="16" width="14" height="12" rx="1" fill="#fff"/><path d="M29 28v14M24 42h10" stroke="#fff" stroke-width="3" fill="none"/></svg>
      <h3>Low Voltage Cabling</h3>
      <p>Clean CAT5 and CAT3 cabling runs for new builds, moves and office upgrades.</p>
    </div>
  </div>
  <div class="band-dots"><span></span><span></span><span></span></div>
</section>

<section class="features">
  <p class="eyebrow">EXPERIENCE ALL</p>
  <h2>Features</h2>
  <div class="feature-grid">
    <div class="feature"><svg viewBox="0 0 26 20"><path d="M7 17a5 5 0 010-10 7 7 0 0113-1 5 5 0 011 11z" fill="#0455a3"/></svg><div><h4>Lorem Ipsum</h4><p>Clear call quality and simple setup for every desk in your office.</p></div></div>
    <div class="feature"><svg viewBox="0 0 26 20"><path d="M7 17a5 5 0 010-10 7 7 0 0113-1 5 5 0 011 11z" fill="#0455a3"/></svg><div><h4>Lorem Ipsum</h4><p>Cloud based lines that grow with your team and your needs.</p></div></div>
    <div class="feature"><svg viewBox="0 0 26 20"><path d="M7 17a5 5 0 010-10 7 7 0 0113-1 5 5 0 011 11z" fill="#0455a3"/></svg><div><h4>Lorem Ipsum</h4><p>Remote access so staff stay reachable from any location.</p></div></div>
    <div class="feature"><svg viewBox="0 0 26 20"><path d="M7 17a5 5 0 010-10 7 7 0 0113-1 5 5 0 011 11z" fill="#0455a3"/></svg><div><h4>Lorem Ipsum</h4><p>Voicemail to email and call routing built into every plan.</p></div></div>
    <div class="feature"><svg viewBox="0 0 26 20"><path d="M7 17a5 5 0 010-10 7 7 0 0113-1 5 5 0 011 11z" fill="#0455a3"/></svg><div><h4>Lorem Ipsum</h4><p>Local technicians ready to help with service and repairs.</p></div></div>
    <div class="feature"><svg viewBox="0 0 26 20"><path d="M7 17a5 5 0 010-10 7 7 0 0113-1 5 5 0 011 11z" fill="#0455a3"/></svg><div><h4>Lorem Ipsum</h4><p>Fair pricing with no hidden fees across all our services.</p></div></div>
  </div>
</section>

<section class="clients" role="img" aria-label="Dark office background behind client testimonials">
  <div class="ring"></div>
  <div class="ring-text">
    <h3>SOME OF OUR CLIENTS</h3>
    <h5>WE LOVE EVERY SINGLE ONE</h5>
    <p>Our new phone system was installed in one day and the team walked every staff member through it. Calls are clearer and support is always quick to answer.</p>
    <p class="author">Jonathan Reed</p>
    <div class="ring-dots"><span></span><span></span><span></span></div>
  </div>
  <div class="client-side">
    <h3>Lorem Ipsum is simply dummy text of the printing and typesetting industry.</h3>
    <ul>
      <li><b>LOREM IPSUM</b><span>Trusted by offices in the region</span></li>
      <li><b>LOREM IPSUM</b><span>Clinics, schools and retailers</span></li>
      <li><b>LOREM IPSUM</b><span>Long term service partners</span></li>
      <li><b>LOREM IPSUM</b><span>Fast and friendly support</span></li>
    </ul>
  </div>
</section>

<section class="gallery">
  <div class="gallery-text">
    <h3>GALLERY</h3>
    <p>A look at recent jobs from our team, from phone system installs to camera setups and structured cabling work for local businesses.</p>
    <span class="btn-outline">VIEW MORE</span>
  </div>
  <div class="tiles">
    <div class="tile t1" role="img" aria-label="Job photo of glowing network lines"></div>
    <div class="tile t2" role="img" aria-label="Job photo of a light blue data display"></div>
    <div class="tile t3" role="img" aria-label="Job photo of purple fiber light"></div>
    <div class="tile t4" role="img" aria-label="Job photo of a blue server room"></div>
    <div class="tile t5" role="img" aria-label="Job photo of a connected city view"></div>
    <div class="tile t6" role="img" aria-label="Job photo of pink fiber optic strands"></div>
  </div>
</section>

<section class="partners">
  <h2>Our Partners</h2>
  <p class="sub">LOREM IPSUM IS SIMPLY DUMMY TEXT OF THE PRINTING.</p>
  <div class="partner-band">
    <span class="arrow" style="left:220px">&#8249;</span>
    <div class="partner-row">
      <span class="partner">Northwave</span>
      <span class="partner">Corliss</span>
      <span class="partner">Vantrell</span>
      <span class="partner">Harbor Lane Group</span>
    </div>
    <span class="arrow" style="right:220px">&#8250;</span>
  </div>
</section>

<section class="contact">
  <div class="contact-head">
    <p>WE WOULD REALLY LOVE TO HEAR FROM YOU!</p>
    <h2>Contact Us</h2>
  </div>
  <div class="contact-photo" role="img" aria-label="Customer support team wearing headsets in a bright office"></div>
  <div class="form-panel">
    <div class="field"><label>Your name <em>required</em></label><div></div></div>
    <div class="field"><label>Your email <em>required</em></label><div></div></div>
    <div class="field"><label>Subject <em>required</em></label><div></div></div>
    <div class="field msg"><label>Message <em>required</em></label><div></div></div>
    <span class="btn">SEND</span>
  </div>
  <div class="info-panel">
    <h3>CONTACT INFO</h3>
    <p class="lead">Lorem Ipsum is simply dummy text of the printing.</p>
    <p class="cta">Contact us for a demo</p>
    <div class="info-item"><svg viewBox="0 0 14 14"><path d="M7 1a4 4 0 014 4c0 3-4 8-4 8S3 8 3 5a4 4 0 014-4z" fill="#0455a3"/></svg><span>2418 Juniper Road<br>Suite 110<br>Maple Falls, OR 97000</span></div>
    <div class="info-item"><svg viewBox="0 0 14 14"><path d="M3 1c1-1 2 0 2 1l1 2c0 1 0 1-1 2 1 2 2 3 4 4 1-1 1-1 2-1l2 1c1 0 2 1 1 2-2 2-5 1-8-2S1 3 3 1z" fill="#0455a3"/></svg><span>(555) 014-2290<br>(555) 014-2291</span></div>
    <div class="info-item"><svg viewBox="0 0 14 14"><rect x="1" y="3" width="12" height="8" fill="none" stroke="#0455a3" stroke-width="1.5"/><path d="M1 3l6 5 6-5" fill="none" stroke="#0455a3" stroke-width="1.5"/></svg><span>hello@amberridgetelecom.example</span></div>
    <div class="map" role="img" aria-label="Street map showing the office location"></div>
  </div>
</section>

<footer class="site-footer">
  <p>© 2024 Amber Ridge Telecom Solutions. All rights reserved.<br>Privacy Policy · Terms of Use</p>
  <div class="to-top" aria-label="Back to top"></div>
</footer>

</body>
</html>
```